i need a business card design for my family investment company "norvane holdings" based in dubai. its a diverse investment firm focusing on education, hospitality and automotive. the design has to be modern and try to incorporate the logo "E" in the design. details on card as follow

Tariq H Bin Rashoud
Managing Director
tariq@norvane.ae
www.norvane.ae

Harbor park,palmcrest tower, office 1730, dubai
tel. 04 3819025
mobile.050 4172958

Target Market(s)

card used for networking events and investor meetings

Industry/Entity Type

Hospitality

```html
<!DOCTYPE html>
<html lang="en">
<head>
<meta charset="utf-8">
<title>Norvane Holdings – Business Card</title>
<link rel="stylesheet" href="https://fonts.googleapis.com/css2?family=Raleway:wght@200;300;400&display=swap">
<style>
  :root {
    --page: #e9e6e1;
    --paper: #ffffff;
    --paper-shade: #eef1f4;
    --ink: #4a4f55;
    --ink-soft: #6b7178;
    --brand-blue: #5b93bb;
    --brand-blue-light: #7fb0d1;
    --brand-blue-deep: #3d6f98;
    --band-blue: #8fb6d2;
  }
  * { box-sizing: border-box; margin: 0; padding: 0; }
  html, body {
    width: 1200px; height: 1023px; overflow: hidden;
    background: var(--page);
    font-family: "Raleway", Arial, sans-serif;
  }
  .canvas { position: relative; width: 1200px; height: 1023px; }

  .card {
    position: absolute; left: 250px; width: 700px; height: 400px;
    border-radius: 4px; overflow: hidden;
    box-shadow: 0 6px 18px rgba(0,0,0,.18);
  }

  /* Front */
  .card-front {
    top: 70px;
    background: linear-gradient(135deg, var(--paper) 0%, var(--paper) 55%, var(--paper-shade) 100%);
  }
  .brand-name {
    position: absolute; left: 48px; top: 44px;
    font-weight: 200; font-size: 40px; letter-spacing: 9px;
    text-transform: uppercase; color: var(--ink);
    display: flex; align-items: center; gap: 18px;
  }
  .brand-mark {
    width: 16px; height: 16px; background: var(--brand-blue-light);
  }
  .holder-name {
    position: absolute; left: 48px; top: 150px;
    font-weight: 300; font-size: 30px; color: var(--brand-blue-light);
  }
  .holder-title {
    position: absolute; left: 50px; top: 196px;
    font-weight: 400; font-size: 14px; letter-spacing: 1px;
    text-transform: uppercase; color: var(--ink-soft);
  }
  .divider {
    position: absolute; left: 48px; right: 48px; top: 236px;
    height: 2px; background: var(--brand-blue-light);
  }
  .contact-list {
    position: absolute; left: 50px; top: 260px; list-style: none;
    font-size: 15px; font-weight: 400; color: var(--ink);
  }
  .contact-list li { display: flex; align-items: center; gap: 12px; height: 26px; }
  .contact-icon { width: 16px; height: 16px; }
  .address {
    position: absolute; right: 48px; top: 260px; text-align: right;
    font-size: 15px; line-height: 26px; color: var(--ink);
  }
  .corner-band {
    position: absolute; left: 0; bottom: 0; width: 260px; height: 22px;
    background: linear-gradient(90deg, var(--band-blue), rgba(143,182,210,0));
  }
  .edge-band {
    position: absolute; left: 0; top: 0; width: 14px; height: 100%;
    background: linear-gradient(180deg, rgba(143,182,210,0), var(--band-blue));
  }

  /* Back */
  .card-back {
    top: 540px;
    background: radial-gradient(ellipse at 60% 45%, var(--brand-blue-light) 0%, var(--brand-blue) 45%, var(--brand-blue-deep) 100%);
  }
  .back-block {
    position: absolute; background: rgba(30,70,110,.14);
  }
  .back-brand {
    position: absolute; inset: 0;
    display: flex; align-items: center; justify-content: center;
    font-weight: 200; font-size: 46px; letter-spacing: 12px;
    text-transform: uppercase; color: #ffffff;
  }
</style>
</head>
<body>
<main class="canvas">

  <section class="card card-front" aria-label="Business card front">
    <div class="edge-band"></div>
    <div class="corner-band"></div>

    <div class="brand-name"><span class="brand-mark"></span>norvane holdings</div>

    <h1 class="holder-name">Tariq H Bin Rashoud</h1>
    <p class="holder-title">Managing Director</p>
    <div class="divider"></div>

    <ul class="contact-list">
      <li>
        <svg class="contact-icon" viewBox="0 0 16 16" aria-hidden="true">
          <rect width="16" height="16" rx="3" fill="var(--ink-soft)"/>
          <path d="M5 4c1 0 1.5 2 1 2.6-.4.4 0 1.4 1.4 2.8 1.4 1.4 2.4 1.8 2.8 1.4.6-.5 2.6 0 2.6 1 0 .8-1 1.4-2 1.4C7 13.2 2.8 9 2.8 5.2 2.8 4.6 4 4 5 4z" fill="#fff"/>
        </svg>
        04 3819025
      </li>
      <li>
        <svg class="contact-icon" viewBox="0 0 16 16" aria-hidden="true">
          <rect width="16" height="16" rx="3" fill="var(--ink-soft)"/>
          <rect x="5" y="3" width="6" height="10" rx="1" fill="none" stroke="#fff" stroke-width="1.2"/>
          <circle cx="8" cy="11.3" r=".7" fill="#fff"/>
        </svg>
        050 4172958
      </li>
      <li>
        <svg class="contact-icon" viewBox="0 0 16 16" aria-hidden="true">
          <rect width="16" height="16" rx="3" fill="var(--ink-soft)"/>
          <rect x="3" y="4.5" width="10" height="7" fill="none" stroke="#fff" stroke-width="1.1"/>
          <path d="M3 4.5l5 4 5-4" fill="none" stroke="#fff" stroke-width="1.1"/>
        </svg>
        tariq@norvane.ae
      </li>
    </ul>

    <address class="address" style="font-style:normal">
      Harbor park, palmcrest tower<br>
      office 1730, dubai<br>
      www.norvane.ae
    </address>
  </section>

  <section class="card card-back" aria-label="Business card back">
    <div class="back-block" style="left:150px; top:0; width:60px; height:36px;"></div>
    <div class="back-block" style="left:240px; top:0; width:40px; height:24px;"></div>
    <div class="back-block" style="left:0; top:300px; width:90px; height:40px;"></div>
    <div class="back-block" style="left:560px; top:352px; width:70px; height:48px;"></div>
    <div class="back-block" style="left:640px; top:330px; width:60px; height:34px;"></div>
    <div class="back-brand">norvane holdings</div>
  </section>

</main>
</body>
</html>
```